Animated (HTML5) banner ad for fantasy football (soccer) app

We want to promote our app where users can:
- Create your fantasy team
- Get points when your players score in real life
- Challenge your friends in private competitions
- Select players from many different leagues: Titans Shield, Crown Circuit, Corvara, Nordmarkpokal, Vetta X, Palme 7, Meridian Trophy, ++
Please have a look here for screenshots and color palette: https://www.sketchvaultz.io/board/qT7xLmR2pWz9KdNvB4hYcE/Clip?frame=0%3A1
Sizes:
1:1 (Square) - 1200 x 1200 pixels.
1.91:1 (Landscape) – 1200 x 628 pixels.
4:5 (Portrait) – 1200 x 1500 pixels.
Prefer the file to be in Google Web Designer, but other might work too.

```html
<!DOCTYPE html>
<html lang="en">
<head>
<meta charset="utf-8">
<title>Fantasy Team Banner Presentation</title>
<link href="https://fonts.googleapis.com/css2?family=Poppins:wght@400;600;700;800&display=swap" rel="stylesheet">
<style>
  :root {
    --canvas: #d9d9d9;
    --caption: #c6373a;
    --orange: #ff9200;
    --white: #ffffff;
    --ink: #141414;
    --sky-top: #0c2a33;
    --sky-mid: #1d5560;
    --ground: #050607;
    --gold: #d9a420;
    --gold-soft: rgba(217,164,32,0);
  }
  * { margin: 0; padding: 0; box-sizing: border-box; }
  html, body { width: 1200px; height: 1200px; overflow: hidden; background: var(--canvas); }
  .board {
    position: relative;
    width: 1200px;
    height: 1200px;
    font-family: "Poppins", sans-serif;
  }
  .board__caption {
    position: absolute;
    top: 95px;
    left: 0;
    width: 100%;
    text-align: center;
    color: var(--caption);
    font-weight: 600;
    font-size: 48px;
    line-height: 60px;
    white-space: nowrap;
  }
  .banner {
    position: absolute;
    left: 221px;
    top: 339px;
    width: 760px;
    height: 760px;
    overflow: hidden;
    color: var(--white);
  }
  .banner__photo {
    position: absolute;
    inset: 0;
    background:
      radial-gradient(ellipse at 60% 40%, rgba(40,110,120,0.55) 0%, rgba(20,60,70,0) 60%),
      linear-gradient(180deg, var(--sky-top) 0%, var(--sky-mid) 30%, #153f48 50%, #0a1518 68%, var(--ground) 100%);
  }
  .banner__ball {
    position: absolute;
    left: 0;
    top: 570px;
    width: 150px;
    height: 190px;
    background: radial-gradient(ellipse at 30% 55%, var(--gold) 0%, rgba(217,164,32,0.6) 45%, var(--gold-soft) 75%);
  }
  .brand {
    position: absolute;
    top: 26px;
    right: 46px;
    font-weight: 700;
    font-size: 40px;
    line-height: 1;
  }
  .headline {
    position: absolute;
    top: 66px;
    left: 0;
    width: 100%;
    text-align: center;
  }
  .headline__intro {
    display: block;
    font-weight: 400;
    font-size: 58px;
    line-height: 66px;
  }
  .headline__main {
    display: block;
    font-weight: 800;
    font-size: 76px;
    line-height: 76px;
    color: var(--orange);
    letter-spacing: -1px;
  }
  .features {
    position: absolute;
    top: 245px;
    left: 0;
    width: 100%;
    list-style: none;
    text-align: center;
  }
  .features__item {
    font-weight: 700;
    font-size: 38px;
    line-height: 49px;
    margin-bottom: 25px;
    white-space: nowrap;
  }
  .features__item em {
    font-style: normal;
    color: var(--orange);
  }
  .cta {
    position: absolute;
    left: 219px;
    top: 624px;
    width: 322px;
    height: 80px;
    border-radius: 18px;
    background: var(--orange);
    color: var(--ink);
    font-weight: 700;
    font-size: 32px;
    display: flex;
    align-items: center;
    justify-content: center;
    text-decoration: none;
  }
</style>
</head>
<body>
  <div class="board">
    <p class="board__caption">I&nbsp; created the HTML animated banner<br>of this design. but could not able to send.</p>

    <main class="banner">
      <div class="banner__photo" role="img" aria-label="Night stadium scene with a footballer silhouetted against a teal cloudy sky, kicking a ball"></div>
      <div class="banner__ball" role="img" aria-label="Shiny gold football in the lower left corner"></div>

      <div class="brand">Rostra</div>

      <h1 class="headline">
        <span class="headline__intro">Create your</span>
        <span class="headline__main">FANTASY TEAM</span>
      </h1>

      <ul class="features">
        <li class="features__item">Get points when your players<br><em>score</em> in real life</li>
        <li class="features__item"><em>Challenge</em> your friends<br>in private competitions</li>
        <li class="features__item">Select players from<br>many <em>different leagues</em></li>
      </ul>

      <a class="cta" href="#">REGISTER NOW</a>
    </main>
  </div>
</body>
</html>
```